Liquor Label / Aguardiente

Label design for liquor bottle. Designers may submit multiple submissions.

Product Description:
Name: Viento de Plata™
Alcohol Category: Aguardiente (which in Spanish most closely translates to “burning water”) – aguardiente is derived from
cane sugar and is a general term for a type of alcoholic spirit in many Central and South America countries.
Taste: A smooth liquor with a comfortable yet spicy finish
Smell: Subtle aroma of spicy jalapeños
Liquid Color: Clear
Bottle Color: Clear
See link for reference - http://www.kelvostamp.com/sites/default/files/styles/uc_product_full/public/Pemrow_0.jpg?itok=9QmT2xLp
Closure: Bar top / cork
Bottle Shape/Size: height = 8.67in; diameter of base = 3.70in; diameter of neck = 0.85in

Label may consist of two separate parts (i.e. front and back, front and vertical side), or one continuous label.

Designer has complete freedom with color, font etc. unless otherwise stated below. The label MUST
contain (but is not limited only to) the following text exactly as written in quotes below:
- “Viento de Plata”
- “Aguardiente”
- “Cane Neutral Spirit with Natural Flavors”
- “35% Alc./Vol.”
- “750 ml”
- “Bottled by WP Spirits, LLC” and “Nashville, TN” - “Government Warning: (1) According to the Surgeon General, women should not drink alcoholic beverages during
pregnancy because of the risk of birth defects. (2) Consumption of alcoholic beverages impairs your ability to
drive a car or operate machinery, and may cause health problems.” (text in previous quotes must be in all
capitalized letters, text must be 2 MM in height and quote must be separated 2MM by all other text)
- Must be dedicated empty space for bar code (approximately 0.75in. height x 1.25in. length)

Target Market(s)

Label should have mass market appeal.
Age: 21 – 28 years old (primary target market is 21+ year old college students and recent graduates)
Target Market Gender: Both male and female, with emphasis on male
Consumption Focus: Spirit will be consumed typically as a shot, primarily at bars and secondarily off premise (label design will be critical for making our product highly visible behind a bar)
Marketing Theme: South American elements. The official Viento de Plata mascot is a llama and the incorporation and use of a llama somewhere (however large or small) on the bottle is encourage but by no means required.

Industry/Entity Type

Health

Requirements
Should not have
• Elements that may lead a potential consumer to believe the beverage is a craft liquor or an artisan brand. Please do not include images of peppers.

```html
<!DOCTYPE html>
<html lang="en">
<head>
<meta charset="utf-8">
<title>Viento de Plata — Aguardiente Label</title>
<link rel="stylesheet" href="https://fonts.googleapis.com/css2?family=Oswald:wght@500;600&family=Lobster&family=Open+Sans:wght@400;700&display=swap">
<style>
  :root {
    --backdrop: #d9d9d9;
    --maroon: #7a2b36;
    --cream: #d6c99a;
    --olive: #3f3d2c;
    --white: #ffffff;
  }
  * { margin: 0; padding: 0; box-sizing: border-box; }
  html, body { width: 1200px; height: 851px; overflow: hidden; }
  body {
    background: var(--backdrop);
    position: relative;
    font-family: "Open Sans", Arial, sans-serif;
    color: var(--olive);
  }

  /* Front label */
  .front-label {
    position: absolute;
    left: 334px; top: 46px;
    width: 531px; height: 652px;
  }
  .front-label .label-shape { position: absolute; inset: 0; }
  .front-label .abs { position: absolute; }

  .mascot-art {
    left: 232px; top: 0;
    width: 76px; height: 122px;
    background: linear-gradient(180deg, #6d6a52 0%, #a7a07c 100%);
  }
  .brand-name {
    font-family: "Oswald", Arial, sans-serif;
    font-weight: 500;
    font-size: 19px;
    line-height: 24px;
    letter-spacing: 0.3px;
    color: var(--olive);
    top: 104px;
    white-space: nowrap;
  }
  .brand-name.left { right: 308px; }
  .brand-name.right { left: 312px; }

  .category {
    left: 154px; top: 190px;
    font-family: "Oswald", Arial, sans-serif;
    font-weight: 600;
    font-size: 16px;
    line-height: 20px;
    color: var(--olive);
    white-space: nowrap;
  }
  .product-title {
    left: -10px; top: 200px; width: 551px;
    text-align: center;
    font-family: "Lobster", cursive;
    font-weight: 400;
    font-size: 102px;
    line-height: 1;
    color: var(--white);
    white-space: nowrap;
    text-shadow:
      1px 1px 0 var(--olive), 2px 2px 0 var(--olive), 3px 3px 0 var(--olive),
      4px 4px 0 var(--olive), 5px 5px 0 var(--olive), 6px 6px 0 var(--olive),
      7px 7px 0 var(--olive), 8px 8px 0 var(--olive),
      -1px 0 0 var(--olive), 0 -1px 0 var(--olive);
  }
  .flavors {
    left: 154px; top: 318px;
    font-family: "Lobster", cursive;
    font-size: 24px;
    line-height: 30px;
    color: var(--olive);
    white-space: nowrap;
  }
  .bottler {
    left: 154px; top: 414px;
    font-family: "Oswald", Arial, sans-serif;
    font-weight: 600;
    font-size: 11.8px;
    line-height: 16px;
    color: var(--olive);
    white-space: nowrap;
  }
  .rule { left: 154px; width: 220px; height: 2px; background: var(--olive); }
  .rule.top { top: 434px; }
  .rule.bottom { top: 465px; }
  .volume {
    left: 154px; top: 438px; width: 220px;
    text-align: center;
    font-size: 15.5px;
    line-height: 24px;
    color: var(--olive);
    white-space: nowrap;
  }
  .warning {
    left: 154px; top: 488px; width: 232px;
    font-size: 10.4px;
    line-height: 20px;
    color: var(--olive);
  }
  .warning strong { display: block; font-weight: 700; }
  .barcode-space {
    left: 420px; top: 483px;
    width: 69px; height: 136px;
    background: var(--white);
  }

  /* Neck strip */
  .neck-strip {
    position: absolute;
    left: 262px; top: 738px;
    width: 675px; height: 66px;
    background: var(--maroon);
  }
  .neck-strip .band {
    position: absolute;
    left: 194px; top: 0;
    width: 283px; height: 66px;
    background: var(--cream);
  }
  .neck-strip .mascot-art {
    position: absolute;
    left: 272px; top: 3px;
    width: 124px; height: 60px;
  }
  .neck-strip .strip-name {
    position: absolute;
    top: 18px;
    font-family: "Oswald", Arial, sans-serif;
    font-weight: 500;
    font-size: 21px;
    line-height: 30px;
    color: var(--cream);
    white-space: nowrap;
  }
  .neck-strip .strip-name.left { left: 26px; }
  .neck-strip .strip-name.right { right: 25px; }
</style>
</head>
<body>

<section class="front-label" aria-label="Front label">
  <svg class="label-shape" width="531" height="652" viewBox="0 0 531 652" aria-hidden="true">
    <path d="M16 0 H515 A16 16 0 0 0 531 16 V636 A16 16 0 0 0 515 652 H16 A16 16 0 0 0 0 636 V16 A16 16 0 0 0 16 0 Z" fill="var(--maroon)"/>
    <rect x="140" y="0" width="250" height="652" fill="var(--cream)"/>
  </svg>

  <div class="abs mascot-art" role="img" aria-label="Engraved llama head mascot illustration"></div>
  <div class="abs brand-name left">VIENTO DE</div>
  <div class="abs brand-name right">PLATA™</div>

  <div class="abs category">CANE NEUTRAL SPIRIT</div>
  <h1 class="abs product-title">Aguardiente</h1>
  <div class="abs flavors">with Natural Flavors</div>

  <div class="abs bottler">BOTTLED BY WP SPIRITS, LLC &amp; NASHVILLE, TN</div>
  <div class="abs rule top"></div>
  <div class="abs volume">750 ML &nbsp;|&nbsp; 35% ALC./VOL.</div>
  <div class="abs rule bottom"></div>

  <p class="abs warning">
    <strong>Government Warning:</strong>
    According to the Surgeon General, women should not drink alcoholic beverages during pregnancy because of the risk of birth defects. Consumption of alcoholic beverages impairs your ability to drive a car or operate machinery, and may cause health problems.
  </p>

  <div class="abs barcode-space" aria-label="Space reserved for barcode"></div>
</section>

<section class="neck-strip" aria-label="Neck label">
  <div class="band"></div>
  <div class="mascot-art" role="img" aria-label="Engraved llama head mascot illustration"></div>
  <div class="strip-name left">VIENTO DE PLATA™</div>
  <div class="strip-name right">VIENTO DE PLATA™</div>
</section>

</body>
</html>
```